Wardens of the Dust Roads book cover

My goal is to choose a submission ready cover for my self-published book. I am looking for an illustrative design that coordinates with the mood of the book, and with current market expectations.

Attached for context are three prior drafts of the cover. My desire is for something more illustrative (like the first one) than obvious AI, like the other two. The story takes place in a fictional town in the Arizona desert. The landscape is a big part of the story. So I would like the mood and color palette to reflect the desert. Reflect; not be a photorealistic depiction of desert. It need not portray the desert explicitly at all, if the design can invoke it. The book does have a fantasy story, but I do not want a "fantasy book" cover. Something more contemporary in design and font choices.

For example, this cover invokes the sea: https://www.bookvendra.example/Tide-Harrow-Novel/dp/100000001X

This one invokes a forest at night: https://www.bookvendra.example/Moss-Lantern-Hour-Pella-Brunwick/dp/1000000022

And this one a different take on the sea: https://www.bookvendra.example/Quiet-Orbit-Novel-Rhys-Dunmore/dp/1000000033

(By the way, my book with its current cover, which I hate, is at:)
https://www.bookvendra.example/Wardens-Dust-Roads-Tom-Kettridge/dp/B000000044

Target Market(s)

25-80 year old, professional females.

Font styles to use
Other font styles liked:
• For the Author Name, use upper and lower case (i.e., Tom Kettridge), with Abadi font, if possible. In the title, make "of the" lower case.

Requirements
Must have
• Copper Wren logo on the spine, with the words "Copper Wren" beneath it.

```html
<!DOCTYPE html>
<html lang="en">
<head>
<meta charset="utf-8">
<title>Wardens of the Dust Roads — Cover</title>
<link rel="stylesheet" href="https://fonts.googleapis.com/css2?family=Cinzel:wght@600;700&family=Marcellus&display=swap">
<style>
  :root {
    --stage: #1c1d19;
    --sky-top: #7cc0ad;
    --sky-mid: #a9d2bb;
    --sky-low: #e6e2c6;
    --sun: #f3ead8;
    --sand: #e3852f;
    --rock: #c23619;
    --rock-deep: #8a1a10;
    --rock-darkest: #5e120c;
    --title-dark: #7c2818;
    --title-red: #a8170f;
    --author: #ecdfc2;
  }
  * { margin: 0; padding: 0; box-sizing: border-box; }
  html, body {
    width: 1200px;
    height: 846px;
    overflow: hidden;
    background: var(--stage);
  }
  .cover {
    position: absolute;
    left: 356px;
    top: 33px;
    width: 488px;
    height: 780px;
    overflow: hidden;
    box-shadow: 0 10px 30px rgba(0, 0, 0, 0.55);
  }
  .cover-art {
    position: absolute;
    inset: 0;
    background:
      radial-gradient(ellipse 120px 110px at 205px 470px, var(--sun) 0%, rgba(243, 234, 216, 0.6) 55%, rgba(243, 234, 216, 0) 100%),
      radial-gradient(ellipse 150px 230px at 360px 560px, rgba(226, 120, 40, 0.75) 0%, rgba(226, 120, 40, 0) 100%),
      linear-gradient(
        to bottom,
        var(--sky-top) 0%,
        var(--sky-mid) 32%,
        var(--sky-low) 55%,
        var(--sand) 63%,
        var(--rock) 74%,
        var(--rock-deep) 88%,
        var(--rock-darkest) 100%
      );
  }
  .title {
    position: absolute;
    left: 0;
    right: 0;
    top: 64px;
    text-align: center;
    line-height: 1;
    font-weight: normal;
  }
  .title span { display: block; }
  .title-top {
    font-family: "Cinzel", serif;
    font-size: 54px;
    font-weight: 700;
    color: var(--title-dark);
    letter-spacing: 0.5px;
  }
  .title-of {
    margin-top: 4px;
    font-family: "Marcellus", serif;
    font-size: 38px;
    color: var(--title-dark);
  }
  .title-main {
    font-family: "Cinzel", serif;
    font-size: 104px;
    font-weight: 600;
    color: var(--title-red);
    letter-spacing: 1px;
  }
  .title-main.first { margin-top: 0; }
  .title-main.second { margin-top: -6px; }
  .author {
    position: absolute;
    left: 0;
    right: 0;
    top: 712px;
    text-align: center;
    font-family: "Marcellus", serif;
    font-size: 40px;
    line-height: 1;
    color: var(--author);
    letter-spacing: 0.5px;
  }
</style>
</head>
<body>
  <main class="cover">
    <div class="cover-art" role="img" aria-label="Illustrated desert landscape: red and orange rock spires and mesas silhouetted against a pale setting sun with radiating rays, under a soft teal sky"></div>
    <h1 class="title">
      <span class="title-top">WARDENS</span>
      <span class="title-of">of the</span>
      <span class="title-main first">DUST</span>
      <span class="title-main second">ROADS</span>
    </h1>
    <p class="author">Tom Kettridge</p>
  </main>
</body>
</html>
```